Business Card

Can you please copy the format provided for the business cards.
Can the logo be in the colours of the last file as specified.

Can the text please be in grey

• Navy Blue: #00457C
• Grey Text: #555555
• Orange Text: #FDBF29

The names on the business card will be

Dorian Pike
0455 718 302
dorian.pike@tallowridgeleasing.example.au

Lvl 7, 14 Harlow Pde
Merrivale QLD 4388
PO Box 3412
Sunhaven MC QLD 9812
P: 1300 742 619
F: 1300 742 638
www.tallowridgeleasing.example.au

And

Leon Whitcombe
0467 590 148
leon.whitcombe@tallowridgeleasing.example.au

Lvl 7, 14 Harlow Pde
Merrivale QLD 4388
PO Box 3412
Sunhaven MC QLD 9812
P: 1300 742 619
F: 1300 743 905

```html
<!DOCTYPE html>
<html lang="en">
<head>
<meta charset="utf-8">
<title>Tallow Ridge Leasing – Business Cards</title>
<link rel="stylesheet" href="https://fonts.googleapis.com/css2?family=Arimo:wght@400;700&display=swap">
<style>
  :root {
    --navy: #00457C;
    --grey-text: #555555;
    --orange: #FDBF29;
    --ink: #222222;
    --name-red: #E3141B;
    --tag-orange: #F05A28;
    --tag-blue: #4A6FB5;
    --card: #FFFFFF;
    --backdrop: #E6E7EA;
    --rule: #333333;
  }
  * { box-sizing: border-box; margin: 0; padding: 0; }
  html, body {
    width: 1200px; height: 1200px; overflow: hidden;
    background: var(--backdrop);
    font-family: "Arimo", Arial, sans-serif;
  }
  .sheet {
    width: 1200px; height: 1200px;
    display: flex; flex-direction: column; align-items: center; justify-content: center;
    gap: 40px;
  }
  .card {
    position: relative;
    width: 900px; height: 540px;
    background: var(--card);
    box-shadow: 0 6px 18px rgba(0,0,0,.15);
    overflow: hidden;
  }
  .card-band {
    position: absolute; left: 0; bottom: 0;
    width: 900px; height: 40px;
  }

  /* front */
  .front-pattern {
    position: absolute; inset: 0 0 40px 0;
    background: linear-gradient(160deg, #F2F4F8 0%, #FFFFFF 55%, #F3F4F7 100%);
  }
  .brand {
    display: flex; align-items: center; gap: 14px;
    color: var(--navy); font-weight: 700; text-transform: uppercase;
  }
  .brand-mark { background: var(--navy); flex: none; }
  .front .brand {
    position: absolute; left: 50%; top: 230px; transform: translateX(-50%);
    font-size: 34px; letter-spacing: 1px; white-space: nowrap;
  }
  .front .brand-mark { width: 56px; height: 56px; }

  /* back */
  .back .brand {
    position: absolute; left: 60px; top: 72px;
    font-size: 24px; letter-spacing: .5px; white-space: nowrap;
  }
  .back .brand-mark { width: 42px; height: 42px; }
  .back-decor {
    position: absolute; right: 0; top: 120px;
    width: 260px; height: 330px;
    background: linear-gradient(135deg, rgba(0,69,124,.07), rgba(253,191,41,.06) 60%, rgba(255,255,255,0));
  }
  .tagline {
    position: absolute; left: 520px; top: 50px;
    font-size: 28px; line-height: 1.1; color: var(--ink);
  }
  .tagline strong { font-weight: 700; }
  .tagline .t-orange { color: var(--tag-orange); }
  .tagline .t-blue { color: var(--tag-blue); }

  .contact { position: absolute; width: 390px; color: var(--ink); }
  .contact-left { left: 60px; top: 210px; }
  .contact-right { left: 490px; top: 175px; }
  .divider {
    position: absolute; left: 470px; top: 170px;
    width: 1px; height: 300px; background: var(--rule);
  }
  .person-name {
    color: var(--name-red); font-weight: 700; font-size: 23px; margin-bottom: 6px;
  }
  .person-line { font-size: 13px; line-height: 1.5; white-space: nowrap; }
  .person-rule { height: 1px; background: var(--rule); margin: 6px 0 14px; }
  .address { font-size: 15px; line-height: 1.45; }
  .numbers { font-size: 15px; line-height: 1.45; margin-top: 14px; }
</style>
</head>
<body>
<main class="sheet">

  <section class="card front" aria-label="Business card front">
    <div class="front-pattern" role="img" aria-label="Faint repeating brand pattern across the card"></div>
    <div class="brand"><span class="brand-mark"></span><span class="brand-name">Tallow Ridge Leasing</span></div>
    <svg class="card-band" viewBox="0 0 900 40" aria-hidden="true">
      <rect x="0" y="0" width="900" height="40" fill="var(--navy)"/>
      <rect x="0" y="0" width="900" height="3" fill="#2F6DB0"/>
      <polyline points="426,40 442,0" stroke="#fff" stroke-width="4" fill="none"/>
      <polyline points="474,40 458,0" stroke="#fff" stroke-width="4" fill="none"/>
    </svg>
  </section>

  <section class="card back" aria-label="Business card back">
    <div class="back-decor" role="img" aria-label="Large faint brand decoration"></div>
    <div class="brand"><span class="brand-mark"></span><span class="brand-name">Tallow Ridge Leasing</span></div>
    <p class="tagline">Steady <strong class="t-orange">LEASING</strong><br>Brighter <strong class="t-blue">ROADS</strong></p>

    <div class="contact contact-left">
      <p class="person-name">Dorian Pike</p>
      <p class="person-line">Phone : 0455 718 302</p>
      <p class="person-line">Email : dorian.pike@tallowridgeleasing.example.au</p>
      <div class="person-rule"></div>
      <p class="address">Lvl 7, 14 Harlow Pde<br>Merrivale QLD 4388<br>PO Box 3412<br>Sunhaven MC QLD 9812</p>
      <p class="numbers">P: 1300 742 619<br>F: 1300 742 638<br>www.tallowridgeleasing.example.au</p>
    </div>

    <div class="divider"></div>

    <div class="contact contact-right">
      <p class="person-name">Leon Whitcombe</p>
      <p class="person-line">Phone : 0467 590 148</p>
      <p class="person-line">Email : leon.whitcombe@tallowridgeleasing.example.au</p>
      <div class="person-rule"></div>
      <p class="address">Lvl 7, 14 Harlow Pde<br>Merrivale QLD 4388<br>PO Box 3412<br>Sunhaven MC QLD 9812</p>
      <p class="numbers">P: 1300 742 619<br>F: 1300 743 905<br>www.tallowridgeleasing.example.au</p>
    </div>

    <svg class="card-band" viewBox="0 0 900 40" aria-hidden="true">
      <rect x="0" y="0" width="900" height="40" fill="var(--navy)"/>
      <rect x="0" y="0" width="900" height="3" fill="#2F6DB0"/>
      <polyline points="426,40 442,0" stroke="#fff" stroke-width="4" fill="none"/>
      <polyline points="474,40 458,0" stroke="#fff" stroke-width="4" fill="none"/>
    </svg>
  </section>

</main>
</body>
</html>
```